New box design for our unique Do-it-Yourself Mushroom Log Kit and Oyster Mushroom Book Recycler Kit

We are looking for a stylish and eye catching design for our range of gourmet mushroom growing kits. The kits are aimed at the gift market and are bought for people who have an interest in growing their own gourmet food and with an interest in mushrooms and mushroom growing.

'Our range of DIY Mushroom Log Kits is attractively packaged containing everything needed to grow gourmet mushrooms using your own logs. With comprehensive, yet easy to follow instuctions, they are ideal for beginners and make interesting gifts and presents for all ages. Each mushroom species can be grown using a wide variety of tree species so the right type of log is easy to find. They are productive, great tasting, and the growing process is both fun and educational.' Three mushroom species: Shiitake, Chicken-of-the-woods, Pearl Oyster.
Webiste link: https://www.fernbrookfungi.co.uk/product-category/mushroom-log-kits/

The 'Oyster Mushroom Book Recyler Kit' is an indoor mushroom growing kit: 'A quick, fun, and easy introduction to gourmet mushroom growing and a novel gift idea too! Taking just twenty minutes to prepare and beginning to crop in as little as two weeks, three crops of oyster mushroom are possible. Once the kit has finished producing indoors, it can then be used to a make an outdoor mushroom bed. Full instructions are included for this nice little gourmet mushroom indoor growing kit.'
Web link: https://www.fernbrookfungi.co.uk/shop/oyster-mushroom-recycler-kits/gourmet-mushroom-indoor-growing-kit/

Box size: 170 mm x 100 mm x 80 mm
Colour scheme should reflect an ecological, natural theme with text areas for descriptions of the mushroom species and how the product works.

Target Market(s)

Gifts for Gardeners, Food Lovers, Home Growing, Mushroom Enthusiasts, Environmentalists, Ecology, Natural Food

Industry/Entity Type

Agriculture

Font styles to use
Decorative

Requirements
Must have
• Images of the mushrooms to be prominent. Inset images to provide backup for the products description and how to use the product.
• Box 1: Oyster Mushroom Book Recycler Kit
• Headline: 'A fun and easy way to grow Gourmet Mushrooms'
• Description:
• 'Turn an old book into a mini mushroom farm! Taking just twenty minutes to prepare and beginning to crop in as little as two weeks, three crops of oyster mushroom are possible. Once the kit has finished producing indoors, it can then be used to a make an outdoor mushroom bed. Full instructions are included'.
• Contents:
• 1 Packet of Oyster Mushroom Grain Spawn
• 1 Filter Grow Bag
• 3 Rubber Bands
• 1 Instruction Sheet
• Storage: Grain Spawn can be stored in the fridge for 3 months and is supplied with a Use-by-Date (see inside).
• Box 2: Shiitake DIY Mushroom Log Kit
• Headline: 'Grow Shiitake Mushrooms Naturally Using Your Own Log'
• Description:
• The quality of Shiitake mushrooms grown naturally using logs is much superior to shop bought mushrooms. They have a richer intense flavour, and a substantial firmer texture, giving the grower a truly authentic gourmet experience. Oak logs are ideal, producing a mushroom crop bi-annually for up to seven years. Other hardwood logs can be used as Shiitake is one of the easiest gourmet mushrooms to grow.
• Contents:
• Plug Spawn: 60 Plugs for 1 x 1m log or 2 x 50 cm logs
• 50g of Soya Wax to seal in the plugs
• 1 x Wax Application Brush
• 1 x 8mm Drill Bit
• Instruction Booklet
• Storage: Plug Spawn can be stored for up to 6 months in a fridge and is supplied with a Use-by-Date (see inside).
• Box 3: Ivory Oyster Log Mushroom Grow Kit
• Headline: 'Grow Pearl Oyster Mushrooms Naturally Using Your Own Log'
• Description:
• Pearl Oyster mushroom is a versatile and productive species making it ideal for beginners. Commonly known as the ‘Tree Oyster’ - a long time favourite of wild mushroom hunters - this winter loving oyster mushroom is easy to grow and delicious to eat, on account of it’s unusually thick and fleshy cap. Great in stir-fries, as a gourmet mushroom pizza topping, or in an oyster mushroom and ale pie.
• Contents:
• 1 x 8mm Drill Bit
• Instruction Booklet
• Box 4: Chicken-of-the-Woods DIY Mushroom Log Kit
• Headline: 'Grow Chicken-of-the-Woods Naturally Using Your Own Log'
• Description:
• Chicken-of-the-woods is an exciting find on summer wild mushroom forays, where it usually found on dead and dying trees. As its name suggests the taste and texture strongly resembles poultry meat, making for a very interesting culinary experience—especially for vegetarians. It can easily be grown using a wide variety of hardwood logs and tree stumps.
• Contents:
• Plug Spawn: 60 Plugs for 1 x 1m log
• 1 x 8mm Drill Bit
• Instruction Booklet
Nice to have
• To be honest, I am not very good at design, so I am for looking for some creative help here, so please feel free to do so. As long as the design is clean, and nicely laid out with attractive fonts, that is my main aim for the product.

```html
<!DOCTYPE html>
<html lang="en">
<head>
<meta charset="utf-8">
<title>Ivory Oyster Log Mushroom Grow Kit – Box Dieline</title>
<link rel="stylesheet" href="https://fonts.googleapis.com/css2?family=Ubuntu:wght@500;700&family=Arimo:wght@700&display=swap">
<style>
  :root{
    --paper:#ffffff;
    --dieline:#d9d9d9;
    --crop:#9a9a9a;
    --ochre:#d6a145;
    --bark-brown:#5c3a1c;
    --leaf-green:#8cc43d;
    --title-green:#1f983d;
    --slate:#5a5a5a;
    --cream:#ffffff;
  }
  html,body{margin:0;padding:0;width:1200px;height:764px;overflow:hidden;background:var(--paper);}
  .sheet{position:relative;width:1500px;height:955px;transform:scale(.8);transform-origin:0 0;font-family:"Ubuntu",sans-serif;}
  .dieline{position:absolute;left:0;top:0;}
  .abs{position:absolute;}
  .title{font-weight:700;font-size:32px;line-height:33px;margin:0;white-space:nowrap;}
  .title .species{color:var(--cream);display:block;}
  .title .kind{color:var(--bark-brown);display:block;}
  .strap{font-weight:700;font-size:15px;line-height:20px;color:var(--cream);margin:12px 0 0;white-space:nowrap;}
  .top-title{font-size:31px;line-height:32px;}
  .top-title .species{color:var(--title-green);}
  .top-strap{color:var(--slate);font-weight:700;font-size:13.5px;line-height:19px;margin:0;white-space:nowrap;}
  .side-head{font-weight:700;font-size:13px;line-height:17px;color:var(--bark-brown);margin:0;white-space:nowrap;}
  .side-copy{font-family:"Arimo",sans-serif;font-weight:700;font-size:6.6px;line-height:10.2px;color:var(--cream);text-align:justify;margin:0;}
  .side-storage{font-family:"Arimo",sans-serif;font-weight:700;font-size:6.6px;line-height:8.4px;color:var(--bark-brown);margin:0;}
  .kit-head{font-weight:700;font-size:12.5px;color:var(--bark-brown);margin:0 0 6px;}
  .kit-list{list-style:none;margin:0;padding:0;font-family:"Arimo",sans-serif;font-weight:700;font-size:6.2px;line-height:7.4px;color:var(--cream);}
  .kit-list li{position:relative;padding-left:8px;margin-bottom:5.5px;}
  .kit-list li::before{content:"✓";position:absolute;left:0;top:0;}
  .photo{position:absolute;}
</style>
</head>
<body>
<div class="sheet">

  <svg class="dieline" width="1500" height="955" viewBox="0 0 1500 955" aria-hidden="true">
    <g stroke="var(--crop)" stroke-width="1" fill="none">
      <line x1="110" y1="47" x2="110" y2="77"/><line x1="64" y1="92" x2="94" y2="92"/>
      <line x1="1413" y1="47" x2="1413" y2="77"/><line x1="1428" y1="92" x2="1458" y2="92"/>
      <line x1="110" y1="855" x2="110" y2="885"/><line x1="64" y1="840" x2="94" y2="840"/>
      <line x1="1413" y1="855" x2="1413" y2="885"/><line x1="1428" y1="840" x2="1458" y2="840"/>
    </g>
    <g stroke="var(--dieline)" stroke-width="1" fill="none">
      <path d="M133 371 V160 H320 L371 295 V371"/>
      <path d="M773 371 V295 L825 160 H1010"/>
      <path d="M1010 371 V92 H1412 V371"/>
      <path d="M110 371 H133 V560 H110 Z"/>
      <path d="M133 560 V640 L185 773 H370 V840 H773 V773 H960 L1010 640 V560"/>
    </g>
    <path d="M1010 135 H1412 V176 C1380 172 1360 180 1330 175 C1300 170 1280 178 1250 174 C1220 170 1200 177 1170 173 C1140 169 1120 176 1090 172 C1060 168 1040 175 1010 171 Z" fill="var(--leaf-green)"/>
    <rect x="133" y="371" width="1279" height="189" fill="var(--ochre)"/>
    <path d="M133 560 V540 C160 532 180 544 210 536 C240 528 260 542 290 534 C320 528 345 540 371 533 C400 528 430 542 460 535 C490 529 520 541 550 535 C580 529 610 542 640 536 C670 530 700 542 730 535 C760 529 790 541 820 535 C850 530 880 541 910 535 C940 529 970 542 1010 534 C1040 528 1070 541 1100 535 C1130 529 1160 542 1190 536 C1220 530 1250 542 1280 535 C1310 529 1340 541 1370 535 C1390 531 1400 536 1412 533 V560 Z" fill="var(--leaf-green)"/>
  </svg>

  <!-- top panel -->
  <div class="photo" role="img" aria-label="Photo of oyster mushrooms growing on a tree stump" style="left:1240px;top:135px;width:172px;height:236px;background:linear-gradient(180deg,#e9ddc6 0%,#c9b08c 35%,#6b5038 60%,#4b3826 100%);"></div>
  <div class="abs" style="left:1028px;top:183px;">
    <h1 class="title top-title"><span class="species">Ivory Oyster</span><span class="kind">Log Mushroom</span><span class="kind">Grow Kit</span></h1>
  </div>
  <p class="abs top-strap" style="left:1028px;top:295px;">Grow Ivory Oyster Mushrooms<br>Outdoors On A Log Of Your Own</p>

  <!-- left side panel -->
  <div class="abs" style="left:150px;top:389px;">
    <p class="side-head">Grow Ivory Oyster Mushrooms<br>Outdoors On A Log Of Your Own</p>
  </div>
  <p class="abs side-copy" style="left:148px;top:430px;width:207px;">The Ivory Oyster is a hardy and generous mushroom, which makes it a great first choice for new growers. Often found on fallen trees in the cooler months, it has long been prized by foragers. It fruits readily on most hardwood logs and rewards you with thick, tender caps full of flavour. Lovely fried in butter, scattered over a homemade pizza, stirred through a risotto or baked into a hearty pie.</p>
  <p class="abs side-storage" style="left:148px;top:509px;width:210px;">Keep it cool: the Plug Spawn will last up to 6 months in a fridge. A Use-by-Date is printed on the pack (see inside).</p>

  <!-- front panel -->
  <div class="abs" style="left:388px;top:380px;">
    <h2 class="title"><span class="species">Ivory Oyster</span><span class="kind">Log Mushroom</span><span class="kind">Grow Kit</span></h2>
    <p class="strap">Grow Ivory Oyster Mushrooms<br>Outdoors On A Log Of Your Own</p>
  </div>
  <div class="photo" role="img" aria-label="Photo of a cluster of oyster mushrooms" style="left:615px;top:425px;width:150px;height:125px;border-radius:45% 50% 40% 45%;background:radial-gradient(ellipse at 50% 40%,#f1e6cf 0%,#d9c29b 55%,#b59468 100%);"></div>

  <!-- right side panel -->
  <div class="photo" role="img" aria-label="Photo of wooden plug spawn dowels" style="left:806px;top:390px;width:72px;height:56px;border-radius:40%;background:radial-gradient(ellipse,#e6e4dc 0%,#b9b6a8 70%,#9ea3a0 100%);"></div>
  <div class="photo" role="img" aria-label="Photo of oyster mushrooms" style="left:800px;top:458px;width:82px;height:72px;border-radius:45%;background:radial-gradient(ellipse at 50% 40%,#efe3cb 0%,#d6bd95 60%,#b39268 100%);"></div>
  <div class="abs" style="left:901px;top:414px;width:100px;">
    <p class="kit-head">In the box</p>
    <ul class="kit-list">
      <li>60 Spawn Dowels: enough for one 1m log or two 50cm logs</li>
      <li>50g Soy Wax to cover each plug hole</li>
      <li>1 x Brush for the wax</li>
      <li>1 x 8mm Wood Drill Bit</li>
      <li>Step-by-Step Guide</li>
    </ul>
  </div>

  <!-- back panel -->
  <div class="abs" style="left:1028px;top:380px;">
    <h2 class="title"><span class="species">Ivory Oyster</span><span class="kind">Log Mushroom</span><span class="kind">Grow Kit</span></h2>
    <p class="strap">Grow Ivory Oyster Mushrooms<br>Outdoors On A Log Of Your Own</p>
  </div>
  <div class="photo" role="img" aria-label="Photo of a cluster of oyster mushrooms" style="left:1255px;top:425px;width:150px;height:125px;border-radius:45% 50% 40% 45%;background:radial-gradient(ellipse at 50% 40%,#f1e6cf 0%,#d9c29b 55%,#b59468 100%);"></div>

</div>
</body>
</html>
```